CRIMSON LANTERN DAY$

We need a postcard to promote a referall program that we are offering to everyone that has purchased a vehicle from us in the past 3 years - - -about 500.
The promotion is titled "crimson Lantern Days" and offers the recipient to earn up to $600, to be passed out the week of Tgiving.

We would require 3 coupons per card 100, 200, 300,and our logo and artwork.
I want it to blast out, catch enough attentioin to read
Front artwork and coupons, back description and rules.

Target Market(s)

our car and truck buyers from the past three years.

Requirements
Must have
• The Front of the postcard should have our Logo, the Promotion and three coupons.
Referal #1 - $100
Referal #2 - $200
Refreal #3 - $300
Each should name the promotion and have a spot for the person refering to write their name.

The back will promote the sale,and provide the timing, and rules.
Nice to have
• fits the excitement of the Season

```html
<!DOCTYPE html>
<html lang="en">
<head>
<meta charset="utf-8">
<title>Crimson Lantern Days Referral Postcard</title>
<link rel="stylesheet" href="https://fonts.googleapis.com/css2?family=Anton&family=Archivo:wght@700;800&display=swap">
<style>
  :root {
    --page: #ffffff;
    --ink: #221f20;
    --red: #e31b23;
    --red-deep: #c8141c;
    --white: #ffffff;
    --silver-hi: #f4f4f4;
    --silver-mid: #b9b9bb;
    --silver-lo: #8a8a8d;
    --label: #555555;
  }
  * { box-sizing: border-box; margin: 0; padding: 0; }
  html, body {
    width: 1200px; height: 1000px; overflow: hidden;
    background: var(--page);
  }
  .postcard {
    position: absolute; left: 65px; top: 82px;
    width: 1072px; height: 830px;
    box-shadow: 10px 12px 18px rgba(0,0,0,0.45);
    overflow: hidden;
  }
  .promo-panel {
    position: absolute; left: 0; top: 0;
    width: 682px; height: 830px;
    background: var(--ink);
    overflow: hidden;
  }
  .promo-stripes { position: absolute; inset: 0; }
  .brand {
    position: absolute; left: 60px; top: 58px;
    display: flex; align-items: center; gap: 14px;
    font-family: "Archivo", Arial, sans-serif;
    font-weight: 800; font-size: 30px; line-height: 1.05;
    color: var(--white);
  }
  .brand-mark { width: 22px; height: 22px; background: var(--red); flex: none; }
  .promo-title {
    position: absolute; left: 80px; top: 345px;
    width: 600px;
    font-family: "Anton", Impact, sans-serif;
    font-weight: 400;
    font-size: 140px; line-height: 0.96;
    text-transform: uppercase;
    transform: rotate(-13deg) skewX(-6deg);
    transform-origin: left top;
  }
  .promo-title .line { display: block; }
  .promo-title .hot {
    color: var(--red);
    text-shadow: 0 0 14px rgba(255,255,255,0.25);
  }
  .promo-title .cool {
    letter-spacing: 34px;
    background: linear-gradient(180deg, var(--silver-hi) 0%, var(--silver-mid) 55%, var(--silver-lo) 100%);
    -webkit-background-clip: text; background-clip: text;
    color: transparent;
  }
  .perforation {
    position: absolute; left: 678px; top: 0; height: 830px;
    border-left: 5px dashed var(--white);
  }
  .coupon-panel {
    position: absolute; left: 685px; top: 0;
    width: 387px; height: 830px;
    background: radial-gradient(ellipse at 40% 50%, #ee2229 0%, var(--red-deep) 100%);
  }
  .coupon {
    position: absolute; left: 0; width: 372px; height: 230px;
    text-align: center;
  }
  .coupon.first { top: 30px; }
  .coupon.second { top: 294px; }
  .coupon.third { top: 556px; }
  .coupon-promo {
    position: absolute; left: 0; right: 0; top: 0;
    font-family: "Archivo", Arial, sans-serif;
    font-weight: 700; font-size: 12px; letter-spacing: 3px;
    color: var(--white); opacity: 0.9;
  }
  .coupon-label {
    position: absolute; left: 0; right: 0; top: 22px;
    font-family: "Archivo", Arial, sans-serif;
    font-weight: 800; font-size: 25px; letter-spacing: 1px; line-height: 1.1;
    color: var(--white);
  }
  .coupon-amount {
    position: absolute; left: 10px; right: 0; top: 50px;
    font-family: "Anton", Impact, sans-serif;
    font-size: 108px; line-height: 1;
    letter-spacing: -1px;
    background: linear-gradient(180deg, var(--silver-hi) 0%, var(--silver-mid) 60%, var(--silver-lo) 100%);
    -webkit-background-clip: text; background-clip: text;
    color: transparent;
    filter: drop-shadow(3px 4px 3px rgba(0,0,0,0.3));
  }
  .coupon-amount sup { font-size: 36px; vertical-align: 52px; margin-right: 4px; }
  .name-field {
    position: absolute; left: 12px; top: 176px;
    width: 338px; height: 50px;
    border-radius: 25px; background: var(--white);
    box-shadow: 2px 3px 4px rgba(0,0,0,0.3);
    font-family: "Archivo", Arial, sans-serif;
    font-size: 10px; color: var(--label);
    text-align: left; padding: 19px 0 0 14px;
  }
  .tear-line {
    position: absolute; left: 0; width: 372px;
    border-top: 4px dashed var(--white);
  }
  .tear-line.first { top: 283px; }
  .tear-line.second { top: 545px; }
</style>
</head>
<body>
  <main class="postcard">
    <section class="promo-panel">
      <svg class="promo-stripes" width="682" height="830" viewBox="0 0 682 830" aria-hidden="true">
        <defs>
          <linearGradient id="silverStreak" x1="0" y1="0" x2="1" y2="0">
            <stop offset="0" stop-color="#9a9a9c"/>
            <stop offset="0.5" stop-color="#f0f0f0"/>
            <stop offset="1" stop-color="#6a6a6c"/>
          </linearGradient>
        </defs>
        <polygon points="0,303 682,140 682,152 0,318" fill="#e31b23"/>
        <polygon points="0,340 655,187 0,365" fill="url(#silverStreak)"/>
        <polygon points="50,830 682,675 682,692 110,830" fill="#e31b23"/>
        <polygon points="160,830 660,708 682,706 682,716 240,830" fill="url(#silverStreak)"/>
      </svg>
      <div class="brand"><span class="brand-mark"></span>HARBOR LANE<br>MOTORS</div>
      <h1 class="promo-title">
        <span class="line hot">Crimson</span>
        <span class="line hot">Lantern</span>
        <span class="line cool">Days</span>
      </h1>
    </section>
    <div class="perforation"></div>
    <section class="coupon-panel">
      <div class="coupon first">
        <p class="coupon-promo">CRIMSON LANTERN DAYS</p>
        <p class="coupon-label">REFERRAL #1</p>
        <p class="coupon-amount"><sup>$</sup>100</p>
        <div class="name-field">NAME:</div>
      </div>
      <div class="coupon second">
        <p class="coupon-promo">CRIMSON LANTERN DAYS</p>
        <p class="coupon-label">REFERRAL #2</p>
        <p class="coupon-amount"><sup>$</sup>200</p>
        <div class="name-field">NAME:</div>
      </div>
      <div class="coupon third">
        <p class="coupon-promo">CRIMSON LANTERN DAYS</p>
        <p class="coupon-label">REFERRAL #3</p>
        <p class="coupon-amount"><sup>$</sup>300</p>
        <div class="name-field">NAME:</div>
      </div>
      <div class="tear-line first"></div>
      <div class="tear-line second"></div>
    </section>
  </main>
</body>
</html>
```